International Wine events organiser seeks simple but stunning business card

I am a freelance events, marketing and PR provider specialised in the Wine industry. I help wineries and wine regions reach trade and consumers in foreign markets through events, help with the websites and communications, press trips and promotional activities. I am looking for a business card which is simple yet effective and is linked to events and communication.

I work mainly - but exclusively - with Italian wineries organising events for them in foreign market.s

I would like to use red in the logo as my present website (lenamorvick.com) used grey and red (although I will be changing the design at a later date).

Target Market(s)

Wine producers, promotional bodies in wine sector, companies looking to hire event organisers,

Industry/Entity Type

Marketing

Requirements
Must have
• My Name - Lena Morvick
My address
My phone
My website : www.lenamorvick.com
my Blog : velvetandtone.me

Should not have
• Butterflies, stars, flowers, anything not particularly linked to wine - would like to keep it simple, modern and eye-catching without being too cliche.

```html
<!DOCTYPE html>
<html lang="en">
<head>
<meta charset="utf-8">
<title>Lena Morvick – Business Card</title>
<link rel="stylesheet" href="https://fonts.googleapis.com/css2?family=Almendra&family=Noto+Serif:wght@400;700&family=Arimo:wght@400&display=swap">
<style>
  :root {
    --page-bg: #ecebe8;
    --card-bg: #ffffff;
    --card-shade: #e4e4e4;
    --orange: #e2441e;
    --orange-deep: #c9301f;
    --red: #d2172b;
    --red-deep: #a8132a;
    --wine: #7c1422;
    --label: #8a1a20;
    --ink: #3e3e3e;
    --soft-ink: #5a5a5a;
  }
  * { margin: 0; padding: 0; box-sizing: border-box; }
  html, body { width: 1200px; height: 750px; overflow: hidden; }
  body { background: var(--page-bg); position: relative; }

  .card {
    position: absolute;
    left: 314px;
    width: 565px;
    height: 334px;
    border-radius: 22px;
    overflow: hidden;
    background: linear-gradient(160deg, var(--card-bg) 45%, var(--card-shade) 100%);
    box-shadow: 0 6px 16px rgba(0,0,0,0.22);
  }
  .card--front { top: 22px; }
  .card--back { top: 396px; background: linear-gradient(200deg, var(--card-bg) 50%, var(--card-shade) 100%); }

  .card__wave { position: absolute; inset: 0; width: 100%; height: 100%; }

  .front__name {
    position: absolute;
    right: 24px;
    top: 162px;
    font-family: "Almendra", serif;
    font-weight: 400;
    font-size: 32px;
    line-height: 40px;
    color: var(--wine);
    white-space: nowrap;
  }
  .front__contacts {
    position: absolute;
    right: 21px;
    top: 247px;
    list-style: none;
    text-align: right;
    font-family: "Noto Serif", serif;
    font-size: 15px;
    line-height: 18.3px;
    color: var(--ink);
    white-space: nowrap;
  }
  .front__label { font-weight: 700; color: var(--label); }

  .brand {
    position: absolute;
    left: 0;
    width: 100%;
    top: 52px;
    display: flex;
    justify-content: center;
    align-items: center;
    gap: 10px;
    transform: translateX(40px);
  }
  .brand__dot { width: 20px; height: 20px; border-radius: 50%; background: var(--red); }
  .brand__name {
    font-family: "Noto Serif", serif;
    font-weight: 700;
    font-size: 26px;
    color: var(--red);
    white-space: nowrap;
  }
  .back__url {
    position: absolute;
    left: 0;
    width: 100%;
    top: 132px;
    text-align: center;
    transform: translateX(94px);
    font-family: "Arimo", sans-serif;
    font-size: 17px;
    color: var(--red-deep);
    white-space: nowrap;
  }
  .back__url, .brand { width: 565px; }
  .back__url { transform: translateX(94px); }
  .services {
    position: absolute;
    left: 205px;
    top: 167px;
    width: 330px;
    font-family: "Noto Serif", serif;
    font-size: 13px;
    color: var(--soft-ink);
    white-space: nowrap;
  }
  .services__title { font-weight: 700; text-align: center; margin-bottom: 17px; }
  .services__list { list-style: none; position: relative; line-height: 20px; font-weight: 700; }
  .services__item--right { position: absolute; left: 232px; top: 0; }
</style>
</head>
<body>
  <section class="card card--front" aria-label="Card front">
    <svg class="card__wave" viewBox="0 0 482 285" preserveAspectRatio="none" aria-hidden="true">
      <path d="M0,0 H482 V58 C380,10 240,-6 160,40 C112,70 118,170 98,188 C78,206 40,175 0,140 Z" fill="var(--orange-deep)"/>
      <path d="M0,0 H482 V30 C380,2 230,-4 150,40 C108,64 112,160 90,176 C64,192 30,160 0,125 Z" fill="var(--orange)"/>
      <path d="M482,42 C380,6 230,6 152,50 C112,74 118,176 96,190 C76,202 40,176 0,142" fill="none" stroke="#ffffff" stroke-width="1.6"/>
    </svg>
    <h1 class="front__name">Lena Morvick</h1>
    <ul class="front__contacts">
      <li><span class="front__label">Tel:</span> 0000000000</li>
      <li><span class="front__label">Web:</span> www.lenamorvick.com</li>
      <li><span class="front__label">Email:</span> hello@lenamorvick.com</li>
      <li><span class="front__label">Blog :</span> velvetandtone.me</li>
    </ul>
  </section>

  <section class="card card--back" aria-label="Card back">
    <svg class="card__wave" viewBox="0 0 482 285" preserveAspectRatio="none" aria-hidden="true">
      <path d="M0,134 C30,110 64,82 88,86 C114,90 112,154 140,180 C182,218 300,236 482,216 V285 H0 Z" fill="var(--red-deep)"/>
      <path d="M0,154 C32,130 68,104 90,108 C112,114 114,172 146,198 C190,232 300,248 482,234 V285 H0 Z" fill="var(--red)"/>
      <path d="M0,143 C30,119 66,92 90,96 C114,100 112,162 142,188 C184,226 300,242 482,225" fill="none" stroke="#ffffff" stroke-width="1.6"/>
    </svg>
    <div class="brand">
      <span class="brand__dot"></span>
      <span class="brand__name">Lena Morvick</span>
    </div>
    <p class="back__url">www.lenamorvick.com</p>
    <div class="services">
      <p class="services__title">Professional help with:</p>
      <ul class="services__list">
        <li>-freelance events</li>
        <li class="services__item--right">-marketing</li>
        <li>-PR provider specialised in the Wine industry</li>
      </ul>
    </div>
  </section>
</body>
</html>
```